High end Coffee Roaster needs a Label design for new Blend

We are looking for a label design for a new blend called "Cold Brew Blend". It is a blend of coffee that we use for making cold brew coffee. The blend is sold as the whole bean and ground coffee in a bag as well as pre-brewed ready to drink in a bottle. We would like the label to be elegant but fun and It must include our logo. Please check out or website brightmilebeans.com or social media @brightmilebeans for information on our company and our coffees if you need more ideas on the kind of product we offer and our style.
Updates

Requirements
Must have
• Our Company Logo. Creative design.
Should not have
• This project should NOT be a corporate company logo, Please do NOT submit a design for a company logo this is a project for a Label. We already have a logo and we are looking for a design on a label. I have uploaded several examples of what we are looking for. Those examples are from other coffee companies who have cold brew. Those are examples only to give you a better idea of what im looking for. DO NOT COPY THEM.

```html
<!DOCTYPE html>
<html lang="en">
<head>
<meta charset="utf-8">
<title>Bright Mile Beans – Cold Brew Coffee Label</title>
<link href="https://fonts.googleapis.com/css2?family=Alegreya:ital,wght@1,400&family=Quicksand:wght@700&display=swap" rel="stylesheet">
<style>
  :root {
    --page: #ffffff;
    --label: #f3f0e7;
    --ink: #5b3a41;
    --blue: #a9c3e6;
    --blue-pale: #cfdcf0;
    --peach: #f5e3d2;
    --cream: #faf1e6;
  }
  html, body {
    margin: 0;
    padding: 0;
    overflow: hidden;
    background: var(--page);
  }
  .canvas {
    position: relative;
    width: 888px;
    height: 1200px;
    background: var(--page);
    overflow: hidden;
  }
  .label {
    position: absolute;
    left: 100px;
    top: 92px;
    width: 693px;
    height: 1010px;
    background: var(--label);
  }
  .brand-dot {
    position: absolute;
    left: 50%;
    top: 130px;
    width: 120px;
    height: 120px;
    margin-left: -60px;
    border: 6px solid var(--ink);
    border-radius: 50%;
    box-sizing: border-box;
  }
  .brand-name,
  .brand-subline {
    position: absolute;
    left: 0;
    right: 0;
    margin: 0;
    text-align: center;
    font-family: "Quicksand", sans-serif;
    font-weight: 700;
    color: var(--ink);
    text-transform: uppercase;
    line-height: 1;
  }
  .brand-name {
    top: 312px;
    font-size: 60px;
    letter-spacing: -0.5px;
  }
  .brand-subline {
    top: 380px;
    font-size: 24px;
    letter-spacing: 30px;
    padding-left: 30px;
  }
  .pattern-band {
    position: absolute;
    left: 0;
    top: 436px;
    width: 100%;
    height: 346px;
    background: linear-gradient(
      to bottom,
      var(--blue) 0%,
      var(--cream) 18%,
      var(--peach) 45%,
      var(--cream) 62%,
      var(--blue) 85%,
      var(--blue-pale) 100%
    );
  }
  .product-name {
    position: absolute;
    left: 0;
    right: 0;
    top: 805px;
    margin: 0;
    text-align: center;
    font-family: "Alegreya", serif;
    font-style: italic;
    font-weight: 400;
    font-size: 74px;
    line-height: 1;
    color: var(--ink);
  }
</style>
</head>
<body>
  <div class="canvas">
    <section class="label">
      <header class="brand">
        <span class="brand-dot"></span>
        <p class="brand-name">Bright Mile</p>
        <p class="brand-subline">Beans</p>
      </header>
      <div class="pattern-band" role="img" aria-label="Decorative band of isometric cubes in pale blue, peach and cream"></div>
      <h1 class="product-name">Cold Brew Coffee</h1>
    </section>
  </div>
</body>
</html>
```